Website layout design UI (not the build)

Hi there, I need a new website designed and before I start the build I want to get the design sorted. I have wireframes for the layout and an array of pics that will be required for the design.
I am looking for a clean contemporary look.

The site will be built using the Salient wordpress theme.

We are a video production company www.kestrelframe.com.au.
The site is designed to enhance our credibility and also drive visitors to a download option (Audio book).
The full brief is in the attached documents, along with pictures, logos, wireframes, sitemaps.

At this point I only need the home page designed. Although I have drafted a wireframe and have included pictures, I'm open to your input to bring this to life and look awesome. Although I'd rather avoid stock images, feel free to make suggestions if need be.

Please read the brief in the attached files before submitting a response.

Thanks Marty

Target Market(s)

Corporate businesses in Australia
Private Schools
Government departments
Not For Profits

Industry/Entity Type

Build

Number of Pages Required

1 page

Font styles to use
Sans Serif

Colors
f04a50

Requirements
Must have
• Clean contemporary look. I'm happy to receive feedback on the suggested content if you think it is too text heavy.
• This will be built using the Salient theme.
• Please review the attached design brief. Also use the assets contained in the zipped file. It includes wireframes, site map (for your info), home page content, pics and logos.
Nice to have
• Relevant icons. Our logo (attached) uses red. So some red inclusion in the design would be good, however it doesn't need to overwhelm. Other colours that are used are grey and black. However feel free to use them minimally.
• Refer to www.kestrelframe.com.au
Should not have
• Busy, ugly layout.

```html
<!DOCTYPE html>
<html lang="en">
<head>
<meta charset="utf-8">
<title>Kestrel Frame – Video Production Sydney</title>
<link href="https://fonts.googleapis.com/css2?family=Roboto:wght@300;400;500;700;900&display=swap" rel="stylesheet">
<style>
:root{
  --red:#f04a50;
  --red-dark:#d93b41;
  --ink:#1f1f1f;
  --text:#555;
  --dark:#3d3d3d;
  --darker:#2c2c2c;
  --mid:#5a5a5a;
  --soft:#f2f2f2;
  --line:#dcdcdc;
  --white:#fff;
}
*{box-sizing:border-box;margin:0;padding:0}
html,body{width:1200px;height:5263px;overflow:hidden}
body{font-family:'Roboto',sans-serif;color:var(--ink);background:var(--white)}
section,header,nav{position:relative;width:1200px}
.abs{position:absolute}
.center{text-align:center}
.section-title{font-size:34px;font-weight:700;text-align:center;color:var(--ink);letter-spacing:.5px}
.frame{border:5px solid var(--red);box-shadow:0 2px 6px rgba(0,0,0,.15)}
.play{position:absolute;left:50%;top:50%;transform:translate(-50%,-50%)}
/* header */
.site-header{height:98px}
.brand{left:147px;top:30px;display:flex;align-items:center;gap:10px}
.brand-dot{width:36px;height:36px;border-radius:50%;background:var(--red)}
.brand-name{font-size:26px;font-weight:900;color:var(--red);letter-spacing:.5px}
.phone{left:672px;top:34px;font-size:22px;font-weight:700;display:flex;align-items:center;gap:8px}
.quote-btn{left:900px;top:28px;width:150px;height:40px;border-radius:20px;background:var(--red);color:#fff;font-size:13px;font-weight:700;display:flex;align-items:center;justify-content:center}
/* hero */
.hero{height:527px;background:linear-gradient(160deg,#6b5a4a 0%,#3d342d 45%,#1e1c1c 100%)}
.hero-title{top:205px;width:100%;text-align:center;color:#fff;font-size:60px;font-weight:700;text-shadow:0 2px 8px rgba(0,0,0,.5)}
.hero-sub{top:290px;left:270px;width:660px;text-align:center;color:#fff;font-size:17px;line-height:1.35;text-shadow:0 1px 4px rgba(0,0,0,.6)}
/* nav */
.main-nav{height:42px;background:var(--red)}
.menu{left:147px;top:0;display:flex;height:42px}
.menu a{color:#fff;font-size:12px;font-weight:700;text-decoration:none;padding:0 13px;display:flex;align-items:center}
.menu a.active{background:var(--red-dark)}
.socials{right:147px;top:11px;display:flex;gap:8px}
.socials span{width:20px;height:20px;border-radius:50%;border:2px solid #fff}
/* partners */
.partners{height:78px;display:flex;justify-content:space-between;align-items:center;padding:0 147px}
.badge{height:40px;background:#d6dbe0;border-radius:4px}
/* media */
.media{height:430px}
.media .video{left:147px;top:55px;width:597px;height:345px}
.ph-video{background:linear-gradient(135deg,#4a4440,#2a2624 60%,#5c4a3c)}
.book{left:800px;top:55px;width:225px;height:230px;background:linear-gradient(120deg,#e9e9e9,#cfcfcf);box-shadow:4px 4px 8px rgba(0,0,0,.25)}
/* about */
.about{height:350px;background:var(--soft)}
.about h2{left:147px;top:55px;font-size:30px;font-weight:700}
.about-copy{left:147px;top:102px;width:410px;font-size:12.5px;line-height:1.5;color:var(--text)}
.about-copy p{margin-bottom:12px}
.about .video{left:590px;top:29px;width:460px;height:270px}
/* services */
.services{height:510px}
.services h2{top:32px;width:100%;font-size:32px;font-weight:700}
.services .kicker{top:78px;width:100%;font-size:26px;font-weight:300;color:var(--red)}
.services .intro{top:126px;left:190px;width:820px;font-size:12.5px;line-height:1.5;color:var(--text)}
.services .lead{top:228px;width:100%;font-size:22px}
.industries{top:300px;left:147px;width:906px;display:flex;justify-content:space-between}
.industry{width:220px;text-align:center}
.industry .disc{width:74px;height:74px;border-radius:50%;background:var(--red);margin:0 auto 12px;display:flex;align-items:center;justify-content:center}
.industry h3{font-size:15px;font-weight:700;margin-bottom:4px}
.industry p{font-size:11.5px;color:var(--text);line-height:1.35}
/* types */
.types{height:372px;background:var(--soft)}
.types h2{top:40px;width:100%}
.type-row{top:112px;left:150px;width:900px;display:flex;justify-content:space-between}
.type{width:215px;text-align:center}
.type .disc{width:175px;height:175px;border-radius:50%;background:var(--mid);margin:0 auto 18px;display:flex;align-items:center;justify-content:center}
.type .disc.red{background:var(--red)}
.type h3{font-size:21px;font-weight:500}
/* testimonials */
.testimonials{height:453px;background:var(--red);color:#fff}
.testimonials h2{top:34px;width:100%;color:#fff}
.quote{top:108px;width:400px;text-align:center}
.quote .avatar{width:80px;height:80px;border-radius:50%;margin:0 auto 18px;background:linear-gradient(135deg,#c89a7a,#6d4a3a);border:3px solid #fff}
.quote p{font-size:12px;line-height:1.5}
.quote .who{margin-top:12px;font-size:12.5px;font-weight:700}
.quote .org{font-size:12px}
.arrow{top:230px;width:28px;height:28px;background:#fff;display:flex;align-items:center;justify-content:center}
.more-link{top:395px;width:100%;font-size:14px;text-decoration:underline;color:#fff}
/* portfolio */
.portfolio{height:807px}
.portfolio h2{top:40px;width:100%}
.grid{top:123px;left:147px;width:906px;display:grid;grid-template-columns:repeat(3,290px);grid-template-rows:repeat(2,275px);column-gap:18px;row-gap:30px}
.grid .tile{position:relative}
.see-more{top:755px;width:100%;font-size:14px;font-weight:700;text-decoration:underline}
/* learn */
.learn{height:333px}
.learn h2{top:48px;width:100%}
.learn-row{top:123px;left:157px;width:918px;display:flex;gap:26px}
.learn-card{flex:none;width:210px;height:178px;border-radius:12px;background:var(--dark);color:#fff;font-size:20px;font-weight:700;display:flex;align-items:center;justify-content:center;text-align:center;padding:0 40px;line-height:1.3}
.learn-card.red{background:var(--red)}
/* blog */
.blog{height:527px;background:linear-gradient(90deg,var(--darker),#4a4a4a 50%,var(--darker))}
.blog h2{top:46px;width:100%;color:#fff}
.posts{top:105px;left:147px;width:906px;display:flex;gap:12px}
.post{width:294px}
.post .thumb{height:225px;background:linear-gradient(135deg,#d9d4cc,#8d8378)}
.post .bar{height:57px;background:var(--red);color:#fff;padding:10px 12px}
.post .bar h3{font-size:16px;font-weight:700}
.post .bar p{font-size:11px;margin-top:3px}
.blog-actions{top:414px;left:147px;width:906px;display:flex;align-items:center}
.pill-dark{width:335px;height:56px;border-radius:28px;background:#111;color:#fff;font-size:15px;font-weight:700;display:flex;align-items:center;justify-content:center}
.search{margin-left:63px;width:440px;height:56px;background:#fff;font-size:14px;color:#888;display:flex;align-items:center;padding-left:16px}
.search-btn{width:68px;height:56px;background:var(--red);display:flex;align-items:center;justify-content:center}
/* download */
.download{height:200px;background:var(--red);color:#fff}
.download h2{top:28px;width:100%;font-size:23px;font-weight:700;line-height:1.35}
.signup{top:120px;left:175px;display:flex;gap:6px}
.field{height:46px;background:#fff;color:#888;font-size:13px;display:flex;align-items:center;padding-left:12px;border-radius:3px}
.btn-black{height:46px;background:#111;color:#fff;font-size:13px;font-weight:700;display:flex;align-items:center;justify-content:center;border-radius:3px}
/* contact */
.contact{height:536px}
.contact h2{top:38px;width:100%}
.contact h3{font-size:21px;font-weight:500}
.map-block{left:147px;top:108px}
.map{margin-top:14px;width:458px;height:232px;background:linear-gradient(135deg,#eae6df,#d5dccf)}
.address{margin-top:22px;display:flex;gap:40px;font-size:12px;line-height:1.5;color:var(--text)}
.enquiry{left:665px;top:108px;width:355px}
.enquiry .field{border:1px solid var(--line);margin-top:12px;height:42px}
.enquiry .field:first-of-type{margin-top:14px}
.enquiry .field.tall{height:52px;align-items:flex-start;padding-top:12px}
.enquiry .btn-black{margin-top:14px;height:46px}
</style>
</head>
<body>

<header class="site-header">
  <div class="abs brand"><span class="brand-dot"></span><span class="brand-name">KESTRELFRAME</span></div>
  <div class="abs phone">
    <svg width="20" height="20" viewBox="0 0 24 24"><path d="M6.6 10.8a15.1 15.1 0 0 0 6.6 6.6l2.2-2.2c.3-.3.7-.4 1-.2 1.1.4 2.3.6 3.6.6.6 0 1 .4 1 1V20c0 .6-.4 1-1 1A17 17 0 0 1 3 4c0-.6.4-1 1-1h3.5c.6 0 1 .4 1 1 0 1.3.2 2.5.6 3.6.1.3 0 .7-.2 1z" fill="#1f1f1f"/></svg>
    +61 2 9000 4821
  </div>
  <div class="abs quote-btn">NEED A QUOTE?</div>
</header>

<section class="hero" role="img" aria-label="Film crew recording a smiling group seated around a table, camera monitor in foreground">
  <h1 class="abs hero-title">Video Production Sydney</h1>
  <p class="abs hero-sub">There has never been a better time to use video production to reach your audience. Professional corporate videos attract attention, engage the audience, build trust, and convert.</p>
</section>

<nav class="main-nav">
  <div class="abs menu">
    <a class="active">HOME</a><a>ABOUT US</a><a>SERVICES</a><a>BLOG PORTFOLIO</a><a>LEARN</a><a>CONTACT</a>
  </div>
  <div class="abs socials"><span></span><span></span><span></span><span></span></div>
</nav>

<section class="partners" aria-label="Client badges">
  <div class="badge" style="width:150px"></div>
  <div class="badge" style="width:150px"></div>
  <div class="badge" style="width:190px"></div>
  <div class="badge" style="width:150px"></div>
  <div class="badge" style="width:110px"></div>
</section>

<section class="media">
  <div class="abs video frame ph-video" role="img" aria-label="Showreel video still of a crew filming an interview">
    <svg class="play" width="80" height="80" viewBox="0 0 80 80"><circle cx="40" cy="40" r="38" fill="#fff"/><path d="M32 24l24 16-24 16z" fill="#333"/></svg>
  </div>
  <div class="abs book" role="img" aria-label="Cover of the book Roll Camera by Marty Halloway, with a director's chair"></div>
</section>

<section class="about">
  <h2 class="abs">ABOUT KESTREL FRAME</h2>
  <div class="abs about-copy">
    <p>Since 1993 Kestrel Frame has been producing impressive corporate videos, videos for government, fundraising videos and school videos.</p>
    <p>We have long been able to use video to tell a stronger story and help our clients reach audiences that matter. Our three step process is based on Strategy, Production and Distribution.</p>
    <p>Your video should align with your goals, enhance your brand and be an appropriate distribution plan, so it can be seen and shared.</p>
  </div>
  <div class="abs video frame ph-video" role="img" aria-label="Video still of a camera operator filming in an office">
    <svg class="play" width="80" height="80" viewBox="0 0 80 80"><circle cx="40" cy="40" r="38" fill="#fff"/><path d="M32 24l24 16-24 16z" fill="#333"/></svg>
  </div>
</section>

<section class="services center">
  <h2 class="abs">VIDEO PRODUCTION SERVICES</h2>
  <p class="abs kicker">VIDEO ROADMAPPING</p>
  <p class="abs intro">The first and essential step in the video production process is having a clear strategy. With Kestrel Frame you get 25 years of video production experience. We understand not only how to make a video, but how to craft a message that connects with your ideal audience. Our video roadmapping service is designed to ensure your video journey starts in the right direction in the right vehicle. Watch this video and visit our roadmapping page to find out more.</p>
  <p class="abs lead">At Kestrel Frame we have expertise in a range of industries:</p>
  <div class="abs industries">
    <div class="industry">
      <div class="disc"><svg width="38" height="38" viewBox="0 0 24 24" fill="#fff"><path d="M12 2 2 7v2h20V7zM4 10h3v8H4zm6.5 0h3v8h-3zM17 10h3v8h-3zM2 19h20v3H2z"/></svg></div>
      <h3>Government Videos</h3><p>Ensure stakeholders are informed and engaged with compelling videos</p>
    </div>
    <div class="industry">
      <div class="disc"><svg width="40" height="40" viewBox="0 0 24 24" fill="#fff"><path d="M12 3 1 9l11 6 9-4.9V17h2V9zM5 13.2v4L12 21l7-3.8v-4L12 17z"/></svg></div>
      <h3>School Videos</h3><p>Raise money, attract enrolments through the community, train staff</p>
    </div>
    <div class="industry">
      <div class="disc"><svg width="36" height="36" viewBox="0 0 24 24" fill="#fff"><path d="M9 3h6a2 2 0 0 1 2 2v2h4a1 1 0 0 1 1 1v11a2 2 0 0 1-2 2H4a2 2 0 0 1-2-2V8a1 1 0 0 1 1-1h4V5a2 2 0 0 1 2-2zm0 4h6V5H9z"/></svg></div>
      <h3>Business Videos</h3><p>Attract more business<br>Train staff<br>Support customers</p>
    </div>
    <div class="industry">
      <div class="disc"><svg width="38" height="38" viewBox="0 0 24 24" fill="#fff"><path d="M12 21 3.5 12.7A5 5 0 0 1 12 5.6a5 5 0 0 1 8.5 7.1z"/></svg></div>
      <h3>Not For Profit</h3><p>Raise funds<br>Find volunteers<br>Tell stories</p>
    </div>
  </div>
</section>

<section class="types">
  <h2 class="abs section-title">WHAT VIDEO PRODUCTION IS RIGHT FOR YOU?</h2>
  <div class="abs type-row">
    <div class="type">
      <div class="disc red"><svg width="90" height="90" viewBox="0 0 24 24" fill="none" stroke="#fff" stroke-width="2"><path d="M3 12 12 3h8v8l-9 9z" fill="#fff" stroke="none"/><circle cx="11" cy="10" r="1.4" stroke="#f04a50" stroke-width="1.3"/><circle cx="14.5" cy="14" r="1.4" stroke="#f04a50" stroke-width="1.3"/><path d="M15.5 9 10 15" stroke="#f04a50" stroke-width="1.3"/></svg></div>
      <h3>Promotional Videos</h3>
    </div>
    <div class="type">
      <div class="disc"><svg width="90" height="90" viewBox="0 0 24 24" fill="none" stroke="#fff" stroke-width="1.6"><circle cx="12" cy="8" r="5"/><path d="M13.3 6.2c-.4-.5-1-.7-1.6-.6-.9.1-1.4.7-1.2 1.3.3.9 2.7.6 2.9 1.7.2.8-.6 1.5-1.6 1.5-.7 0-1.3-.3-1.6-.8M12 4.6v1m0 4.8v1"/><path d="M3 17h4l4 2h5l4-3M7 17v4"/></svg></div>
      <h3>Fundraising Videos</h3>
    </div>
    <div class="type">
      <div class="disc"><svg width="90" height="90" viewBox="0 0 24 24" fill="none" stroke="#fff" stroke-width="1.6"><rect x="8" y="4" width="13" height="9"/><circle cx="5" cy="9" r="2" fill="#fff"/><path d="M3 20v-5c0-1.2 1-2 2-2h2l4-2M9 20v-4"/></svg></div>
      <h3>Training Videos</h3>
    </div>
    <div class="type">
      <div class="disc"><svg width="90" height="90" viewBox="0 0 24 24" fill="#fff"><rect x="4" y="6" width="12" height="8" rx="1"/><path d="M16 8.5l4-2.5v8l-4-2.5z"/><path d="M10 14v3m0 0-4 5m4-5 4 5" stroke="#fff" stroke-width="1.5" fill="none"/></svg></div>
      <h3>Live Events</h3>
    </div>
  </div>
</section>

<section class="testimonials">
  <h2 class="abs section-title">CLIENT TESTIMONIALS</h2>
  <div class="abs arrow" style="left:108px"><svg width="12" height="12" viewBox="0 0 12 12"><path d="M8 1 3 6l5 5" stroke="#f04a50" stroke-width="2" fill="none"/></svg></div>
  <div class="abs quote" style="left:170px">
    <div class="avatar" role="img" aria-label="Client portrait"></div>
    <p>Lorem ipsum dolor sit amet, consectetuer adipiscing elit, sed diam nonummy nibh euismod tincidunt ut laoreet dolore magna aliquam erat volutpat. Ut wisi enim ad minim veniam, quis nostrud exerci tation ullamcorper suscipit lobortis nisl ut aliquip ex ea commodo consequat.</p>
    <p class="who">Mr. Reed A.</p><p class="org">Kestrel Frame, CA</p>
  </div>
  <div class="abs quote" style="left:630px">
    <div class="avatar" role="img" aria-label="Client portrait"></div>
    <p>Lorem ipsum dolor sit amet, consectetuer adipiscing elit, sed diam nonummy nibh euismod tincidunt ut laoreet dolore magna aliquam erat volutpat. Ut wisi enim ad minim veniam, quis nostrud exerci tation ullamcorper suscipit lobortis nisl ut aliquip ex ea commodo consequat.</p>
    <p class="who">Ms. Tara W.</p><p class="org">Kestrel Frame, CA</p>
  </div>
  <div class="abs arrow" style="left:1064px"><svg width="12" height="12" viewBox="0 0 12 12"><path d="m4 1 5 5-5 5" stroke="#f04a50" stroke-width="2" fill="none"/></svg></div>
  <p class="abs more-link center">Other Testimonials</p>
</section>

<section class="portfolio">
  <h2 class="abs section-title">PORTFOLIO</h2>
  <div class="abs grid">
    <div class="tile frame ph-video" role="img" aria-label="Portfolio video: crew filming a seated interview"><svg class="play" width="70" height="70" viewBox="0 0 80 80"><circle cx="40" cy="40" r="38" fill="#fff"/><path d="M32 24l24 16-24 16z" fill="#333"/></svg></div>
    <div class="tile frame ph-video" role="img" aria-label="Portfolio video: studio set with lights"><svg class="play" width="70" height="70" viewBox="0 0 80 80"><circle cx="40" cy="40" r="38" fill="#fff"/><path d="M32 24l24 16-24 16z" fill="#333"/></svg></div>
    <div class="tile frame ph-video" role="img" aria-label="Portfolio video: presenter speaking to camera"><svg class="play" width="70" height="70" viewBox="0 0 80 80"><circle cx="40" cy="40" r="38" fill="#fff"/><path d="M32 24l24 16-24 16z" fill="#333"/></svg></div>
    <div class="tile frame ph-video" role="img" aria-label="Portfolio video: director reviewing footage"><svg class="play" width="70" height="70" viewBox="0 0 80 80"><circle cx="40" cy="40" r="38" fill="#fff"/><path d="M32 24l24 16-24 16z" fill="#333"/></svg></div>
    <div class="tile frame ph-video" role="img" aria-label="Portfolio video: camera operator at work"><svg class="play" width="70" height="70" viewBox="0 0 80 80"><circle cx="40" cy="40" r="38" fill="#fff"/><path d="M32 24l24 16-24 16z" fill="#333"/></svg></div>
    <div class="tile frame ph-video" role="img" aria-label="Portfolio video: filming in a kitchen"><svg class="play" width="70" height="70" viewBox="0 0 80 80"><circle cx="40" cy="40" r="38" fill="#fff"/><path d="M32 24l24 16-24 16z" fill="#333"/></svg></div>
  </div>
  <p class="abs see-more center">SEE MORE OF OUR WORK</p>
</section>

<section class="learn">
  <h2 class="abs section-title">LEARN VIDEO PRODUCTION</h2>
  <div class="abs learn-row">
    <div class="learn-card red">FREE Roll Camera Audiobook</div>
    <div class="learn-card">Roll Camera book</div>
    <div class="learn-card">KFA online course</div>
    <div class="learn-card">Live workshop</div>
  </div>
</section>

<section class="blog">
  <h2 class="abs section-title">LATEST BLOG</h2>
  <div class="abs posts">
    <div class="post"><div class="thumb" role="img" aria-label="Hands writing on paper at a desk"></div><div class="bar"><h3>IDENTIFY THE ISSUES</h3><p>We help you break down your biggest problems</p></div></div>
    <div class="post"><div class="thumb" role="img" aria-label="Business team meeting around a laptop"></div><div class="bar"><h3>STRUCTURED ADVICE</h3><p>We give you clear legal advice about your options</p></div></div>
    <div class="post"><div class="thumb" role="img" aria-label="Person reviewing charts on paper"></div><div class="bar"><h3>RESEARCH &amp; ANALYSIS</h3><p>We examine your case to find the best solution</p></div></div>
  </div>
  <div class="abs blog-actions">
    <div class="pill-dark">Check out more articles or search here</div>
    <div class="search">Search here...</div>
    <div class="search-btn"><svg width="26" height="26" viewBox="0 0 24 24" fill="none" stroke="#fff" stroke-width="2.4"><circle cx="10" cy="10" r="6.5"/><path d="m15 15 6 6"/></svg></div>
  </div>
</section>

<section class="download">
  <h2 class="abs center">DOWNLOAD FREE AUDIO BOOK OF<br>BESTSELLER ROLL CAMERA</h2>
  <div class="abs signup">
    <div class="field" style="width:280px">Your Name</div>
    <div class="field" style="width:285px">Email</div>
    <div class="btn-black" style="width:275px">GET THE FREE AUDIOBOOK</div>
  </div>
</section>

<section class="contact">
  <h2 class="abs section-title">CONTACT US</h2>
  <div class="abs map-block">
    <h3>Map</h3>
    <div class="map" role="img" aria-label="Street map with a location pin at the office"></div>
    <div class="address">
      <p>Kestrel Frame Pty Ltd<br>Suite 3, 18 Larkin St<br>Epping NSW 2121</p>
      <p>Ph: +61 2 9000 4821<br>info@kestrelframe.com.au</p>
    </div>
  </div>
  <div class="abs enquiry">
    <h3>Enquiry form</h3>
    <div class="field">Your Name</div>
    <div class="field">Email</div>
    <div class="field">Phone</div>
    <div class="field tall">Query</div>
    <div class="btn-black">SUBMIT NOW</div>
  </div>
</section>

</body>
</html>
```